Packaging Design for Fruit Juice Product

The Product is a fruit juice product. Kindly refer to the photograph attached for the temporary bottle shape and label position. (Please note that the cap colour will be different (not green), as it will be adjusted with the label design)

The fruit is Carica (it's similar like Papaya, but just in yellow color and smaller size). Like the other juice products, the target market covers most of the age range from 10 - 60 years old.

The temporary product name is: KEM

The fact that this juice product is quite unique, I want the product design to be something revolutionary and 'epic'.
The graphic design could be anything depends on your imagination. Basically, I want you to expand your creativity in designing the logo and the overall graphic design for the label.

- Do not design something ordinary or mediocre. Be Extraordinary -

*****The information below may / may not be used to base the label design. It is all up to you to decide whether it is useful in designing the label or not*****

I also have attached the basic information of the fruit and the place where the Carica tree grows: Dieng Plateau.
Dieng Plateau is Highland area where there are mountains. This Dieng Plateau is believed to be the place where the Gods live in the past.
This is probably because of the beautiful landscapes and the epic nature gift such as multi colour lakes, Volcanic crater, etc. (There are lots of myth about this place anyway).
Updates

There are lots of amazing and absolutely great designs on these websites:
You may want to check for the inspiration of our Fruit Juice Project 

Industry/Entity Type

Graphic Design

Requirements
Must have
• Remarkable logo and graphic design.

```html
<!DOCTYPE html>
<html lang="en">
<head>
<meta charset="utf-8">
<title>KEM Juice Label</title>
<link href="https://fonts.googleapis.com/css2?family=Source+Sans+3:wght@400;600;700;900&display=swap" rel="stylesheet">
<style>
:root{
  --teal:#0aa0b4;
  --teal-dark:#0c5b66;
  --ink:#114a55;
  --white:#ffffff;
  --panel:rgba(255,255,255,0.72);
  --stage:#f7f7f9;
  --sun:#ffd800;
  --orange:#f7a021;
  --purple:#4a2580;
  --green:#3db54a;
  --deep-teal:#0097a7;
}
*{margin:0;padding:0;box-sizing:border-box}
html,body{width:1200px;height:1000px;overflow:hidden;background:var(--white);font-family:"Source Sans 3",sans-serif}
.canvas{position:relative;width:1200px;height:1000px}
.stage{position:absolute;left:60px;top:32px;width:1052px;height:546px;background:var(--stage)}
.label{position:absolute;left:121px;top:88px;width:959px;height:442px;overflow:hidden}
.landscape{position:absolute;inset:0;background:
  linear-gradient(180deg,rgba(255,255,255,0) 0%,rgba(255,255,255,0) 62%,rgba(28,160,120,0.9) 75%,#0f9a6a 100%),
  radial-gradient(ellipse at 50% 5%,#fffbe0 0%,#fff07a 35%,#f6d400 70%,#ffc800 100%);}
.hills{position:absolute;left:0;right:0;top:150px;height:170px;background:linear-gradient(180deg,#c9e7a5,#8fcf8a 60%,#4cb7a6);opacity:.7;border-radius:50% 50% 0 0/30% 30% 0 0}
.nutrition{position:absolute;left:3px;top:10px;width:238px;height:327px;background:var(--panel);border-radius:14px;padding:3px 6px;color:var(--ink);font-size:11px;line-height:1.2}
.nutrition h2{color:var(--teal);font-size:20px;font-weight:700;text-align:center;line-height:1}
.nutrition .serving{font-size:12px;letter-spacing:.6px;line-height:1.05}
.row{display:flex;justify-content:space-between;border-top:1px solid var(--teal);padding:1px 4px}
.row.thick{border-top:3px solid var(--teal)}
.row.indent{padding-left:40px}
.row.indent2{padding-left:20px}
.row b{font-weight:700}
.vitamins{text-align:center;border-top:3px solid var(--teal);padding-top:2px}
.note{font-size:11.5px;margin-top:4px}
.fruit{position:absolute;left:226px;top:175px;width:132px;height:150px;border-radius:50%;background:radial-gradient(circle at 40% 40%,#ffb54a,#f08a12)}
.slogan{position:absolute;left:260px;top:94px;width:98px;text-align:right;color:var(--ink);font-weight:700;font-size:19px;line-height:1.15;letter-spacing:.5px}
.brand{position:absolute;left:350px;top:118px;width:340px;text-align:center;font-weight:900;font-size:150px;line-height:1;color:var(--orange)}
.badge{position:absolute;left:600px;top:33px;width:96px;height:96px;border-radius:50%;background:radial-gradient(circle,#fff35a 50%,rgba(255,240,90,.3));color:#1d7a2d;text-align:center;font-weight:700;padding-top:26px;transform:rotate(8deg)}
.badge .pct{font-size:21px;line-height:1}
.badge .word{font-size:14px}
.ingredients{position:absolute;left:699px;top:40px;width:248px;height:268px;background:var(--panel);border-radius:14px;padding:18px 12px;color:var(--ink)}
.ingredients h2{color:var(--teal);font-size:22px;font-weight:400;text-align:center;margin-bottom:14px}
.ingredients p{font-size:13px;line-height:1.3;text-align:justify}
.net{position:absolute;left:607px;top:342px;color:var(--white);line-height:1}
.net .oz{font-size:16px;font-weight:600}
.net .ml{font-size:26px}
.footline{position:absolute;left:12px;top:396px;color:var(--white);font-size:17px;letter-spacing:.4px}
.address{position:absolute;right:16px;top:372px;text-align:right;color:var(--white);font-size:13px;font-weight:600;letter-spacing:1px;line-height:1.35}
.band{position:absolute;left:0;top:578px;width:1200px;height:422px;background:linear-gradient(30deg,var(--deep-teal) 0%,#0aa88a 45%,var(--green) 100%)}
.band-brand{position:absolute;left:720px;top:60px;width:420px;text-align:center;font-weight:900;font-size:230px;line-height:1.2;color:var(--orange)}
</style>
</head>
<body>
<div class="canvas">
  <div class="stage"></div>
  <div class="label">
    <div class="landscape" role="img" aria-label="Highland scene with rising sun, green hills, lake and pine trees"></div>
    <div class="nutrition">
      <h2>Nutrition Facts</h2>
      <div class="serving">Serving Size 15.8 FL Oz (468 mL)<br>Servings Per Container about 4</div>
      <div class="row thick"><b>Amount per Serving</b></div>
      <div class="row"><span><b>Calories</b> 150</span><span>Calories from Fat 10</span></div>
      <div class="row" style="border:0;justify-content:flex-end"><b>% Daily Value</b></div>
      <div class="row thick"><span><b>Total Fat</b> 1g</span><b>2%</b></div>
      <div class="row indent"><span>Saturated Fat 0.5g</span><b>3%</b></div>
      <div class="row indent"><i>Trans Fat 0g</i></div>
      <div class="row thick"><span><b>Cholesterol</b> 0mg</span><b>0%</b></div>
      <div class="row"><span><b>Sodium</b> 104mg</span><b>4%</b></div>
      <div class="row"><span><b>Potassium</b> 230mg</span><b>7%</b></div>
      <div class="row thick"><span><b>Total Carbohydrate</b> 28g</span><b>9%</b></div>
      <div class="row indent"><span>Dietary Fiber 0g</span></div>
      <div class="row indent"><span>Sugars 20g</span></div>
      <div class="row indent2"><span><b>Protein</b> 7g</span><b style="margin-right:20px">14%</b></div>
      <div class="vitamins">Vitamin A 2% &nbsp;•&nbsp; Vitamin C 160%<br>Calcium 2% &nbsp;•&nbsp; Iron 15%</div>
      <div class="note">· Percent Daily Values are based on a 2,000 calorie diet.</div>
    </div>
    <div class="fruit" role="img" aria-label="Whole and sliced carica fruit illustration"></div>
    <div class="slogan">NO<br>SUGAR<br>ADDED</div>
    <div class="brand">KEM</div>
    <div class="badge"><div class="pct">100%</div><div class="word">NATURAL</div></div>
    <div class="ingredients">
      <h2>INGREDIENTS:</h2>
      <p>Lorem, Ipsum dolor, Sit amet, Luctus Dui, Mol Uris Sodales, Felis, the Quick Brown Fox, Jumps, Over, Lorem, Ipsum dolor, Sit amet, Luctus Dui, Mol Uris Sodales, Felis, the Quick Brown Fox, Jumps, Over, Lorem, Ipsum dolor, Sit amet, Luctus Dui, Mol Uris Sodales, Felis, the Quick Brown Fox, Jumps, Over, Lorem, Ipsum dolor, Sit amet, Luctus, Lorem, Dui, Dolor</p>
    </div>
    <div class="net"><div class="oz">NET 15.8 FL OZ</div><div class="ml">468 mL</div></div>
    <div class="footline">SHAKE WELL &nbsp;•&nbsp; PERISHABLE (Keep Refrigerated) &nbsp;•&nbsp; No Preservatives</div>
    <div class="address">48 Orchard Lane,<br>Hillview, NY, 10482<br>www.kemjuice.example</div>
  </div>
  <div class="band">
    <div class="band-brand">KEM</div>
  </div>
</div>
</body>
</html>
```